Velvet Ink Studio - Semi Permanent Makeup

Website Brief
Overview:
• Product - Cosmetics Tattooing \ Permanent Makeup
• Permanent beauty services including permanent eyebrow hairstrokes, eyeliner, lip liner, Lip Blend
• Marketing - over 18 year old women
• Website pages: Home – Services - About Rosalind – Pricing – Contact Us – Pre Procedures - Post Procedures (please read below for page titles in purple)
• There is logo and design all be done by artist hive and should be on file
Home Page
Pictures:
Logo: as per attachment
Slogan:
Special Offers:
Facebook: Setup and link on web page
Testimonials: What people are saying, Commits from clients
Marking box\Banner: that flicks around with either special offices, testimonials, location of Rosalind, slogans etc..
Services
Semi - Permanent Makeup
Eyebrows:
o Summary
o Before, After and healed pictures
Upper and Lower Eyeliner
o Summary
Lip Liner:
o Summary

Lip Blend:
o Summary
Corrections:
o Summary
Tattoo Removal:
o Summary

About Rosalind:
o Summary

Rosalind Studied Certificate:
QRTMVNP617C – Design and perform cosmetic tattooing
KMDPR719E – Maintain infection control standards in office practice setting
JPWCFE118 – Provide First Aid
Business Management - Frontline Management
Graduate Diploma - Project Management
Pricing:
Price List
Semi - Permanent Eyebrow Hairstrokes $430.00
Permanent Upper Eyeliner $420.00
Permanent Lower Eyeliner $420.00
Upper & Lower Eyeliner together $580.00
Lip Liner $360.00
Lip Blend $450.00
Tattoo Removal session $199.00
Consultation Free
• A follow-up appointment is included in all services within 4 to 6 weeks.

Aftercare Procedures Procedures:
o Summary
Contact Us:
Subscribe to mailing list:
o Email address
Contact Velvet Ink Studio:
• Name
• Phone
• Email address
• Preferred Contact Method
• Subscribe to newsletter , special offers and events
Location:
• By email: velvetinkstudio@maildrop.example
• By Phone:
o 0219374620
• Facebook: Velvet Ink Studio
• Address: 47 Fernleigh Crescent, Tui Harbour, 8093, Christchurch

Reason: I have extended the dead line as I have been working 7days a week and given that some of the communication is restricted to due to time difference. I need extra time. Thanks to all design I will be back to shortly.

Target Market(s)

Over 18 years, all ages main females, but I do get a small amount of men

Industry/Entity Type

Tattoo

Coding

Coded - Design and coding required

Number of Pages Required

5+ page

Font styles to use
Sans Serif

Requirements
Must have
• Home page
• Services page
• About Rosalind page
• Pricing – Contact Us page
• Pre Procedures - Post care procedures page
• I would client to be able to subscribe to new letter
• Please go to my facebook page - Velvet Ink Studio - Christchurch, as the banner I have here, I would like to see on my webpage
Nice to have
• Please go on to my Facebook page as there client picture that could be used Velvet Ink Studio
• Before and after pictures
• Eyeliner
• Lip Liner
• Lip Blend
• Eyebrow Hair stroke
• The first two site below are my direct competitors, so I wold like something that is better that these:
• New Zealand:
• http://www.glowinglashlines.example.nz/
• http://www.browcraftery.example.nz/

```html
<!DOCTYPE html>
<html lang="en">
<head>
<meta charset="utf-8">
<title>Velvet Ink Studio – Semi Permanent Makeup</title>
<link rel="stylesheet" href="https://fonts.googleapis.com/css2?family=Open+Sans:ital,wght@0,400;0,600;0,700;1,400&family=Oswald:wght@400;500&family=Dancing+Script:wght@500&display=swap">
<style>
:root{
  --paper:#ecebe5;
  --ink:#000;
  --white:#fff;
  --blue:#2a9fd8;
  --blue-light:#6cc3ee;
  --text:#555;
  --muted:#8a8a8a;
  --row:#d7ebf6;
  --sky:#bcd9e6;
  --night:#1d1d1d;
}
*{box-sizing:border-box;margin:0;padding:0}
html,body{width:1200px;height:4235px;overflow:hidden}
body{position:relative;background:var(--paper);font-family:"Open Sans",Arial,sans-serif;color:var(--text)}
.abs{position:absolute}

/* header / hero */
.hero{left:0;top:0;width:1200px;height:632px;background:var(--white)}
.brand{left:196px;top:36px;display:flex;align-items:center;gap:10px}
.brand-dot{width:22px;height:22px;border-radius:50%;background:var(--ink)}
.brand-name{font:600 22px "Open Sans",sans-serif;color:var(--ink)}
.nav{left:436px;top:55px;display:flex;gap:24px;font:400 12.5px "Oswald",sans-serif;color:#555;letter-spacing:.3px}
.hero-art{left:300px;top:92px;width:720px;height:540px;
  background:radial-gradient(ellipse at 62% 40%,#f1c9ae 0,#e9b59a 28%,#f0b8c8 50%,#f6dbe3 68%,rgba(255,255,255,0) 85%)}
.slogan{font:500 40px "Dancing Script",cursive;color:#7a7a7a}
.slogan-1{left:130px;top:300px}
.slogan-2{left:190px;top:352px}

/* offer band */
.offer{left:0;top:632px;width:1200px;height:125px;background:var(--ink)}
.offer-badge{left:186px;top:630px;width:80px;height:142px}
.offer-badge-text{left:186px;top:668px;width:80px;text-align:center;font:500 15px/1.15 "Oswald",sans-serif;color:var(--white)}
.offer-text{left:292px;top:666px;font:400 34px "Open Sans",sans-serif;color:var(--white)}
.offer-text b{color:var(--blue);font-weight:400}

/* tabs */
.tab{height:56px;padding:0 22px;background:var(--blue);outline:4px solid var(--blue-light);outline-offset:-4px;
  font:500 22px/56px "Oswald",sans-serif;color:var(--white);text-transform:uppercase;letter-spacing:.5px;
  box-shadow:6px -6px 0 var(--blue-light)}
.tab-note{font:400 13px "Open Sans",sans-serif;color:#555}

/* panels */
.panel{background:var(--ink)}
.fb-box{left:250px;top:905px;width:282px;height:222px;background:var(--white);padding:10px}
.fb-head{height:84px;background:linear-gradient(#6b6b6b,#3a3a3a);position:relative}
.fb-title{position:absolute;left:58px;top:10px;font:700 13px "Open Sans",sans-serif;color:var(--white)}
.fb-likes{position:absolute;left:58px;top:28px;font:400 10px "Open Sans",sans-serif;color:#ddd}
.fb-thumb{position:absolute;left:8px;top:8px;width:42px;height:42px;background:#ccc}
.fb-btn{position:absolute;bottom:8px;height:18px;padding:0 8px;background:#f2f2f2;border:1px solid #bbb;font:600 9px/16px "Open Sans",sans-serif;color:#333}
.fb-photo{height:64px;margin-top:4px;background:linear-gradient(90deg,#9d8f86,#c8b8ae,#7e7370)}
.fb-foot{margin-top:8px;font:400 9px "Open Sans",sans-serif;color:#777}
.fb-faces{display:flex;gap:4px;margin-top:6px}
.fb-faces i{width:26px;height:26px;background:#cfc5bf}

.quote{left:660px;top:912px;width:310px;font:italic 400 11.5px/1.55 "Open Sans",sans-serif;color:#ddd}
.avatar{left:712px;top:990px;width:100px;height:100px;border-radius:50%;border:4px solid #fff;background:radial-gradient(circle at 50% 45%,#f0c8a8,#e4b46a 60%,#caa063)}
.quote-name{left:826px;top:1030px;font:400 12px "Open Sans",sans-serif;color:var(--blue)}
.arrow{font:700 20px "Open Sans",sans-serif;color:var(--blue)}

/* services */
.services-band{left:0;top:1262px;width:1200px;height:610px;background:var(--ink)}
.services-sub{left:404px;top:1210px;font:400 27px "Open Sans",sans-serif;color:#444}
.card{width:264px;height:250px}
.card-top{height:135px;background:var(--white);padding:10px 12px}
.card-head{display:flex;align-items:center;gap:8px;height:24px}
.card-title{font:400 14px "Open Sans",sans-serif;color:var(--blue)}
.card-text{margin-top:6px;font:400 10.5px/1.45 "Open Sans",sans-serif;color:#555}
.card-text b{color:var(--blue);font-weight:400}
.card-photo{height:88px;display:flex}
.card-photo span{flex:1}
.card-labels{display:flex;justify-content:space-between;padding:5px 4px 0;font:400 13px "Open Sans",sans-serif;color:var(--white)}

/* about */
.about-intro{left:186px;top:1932px;width:580px;font:400 11.5px/1.5 "Open Sans",sans-serif;color:#888}
.about-photo{left:186px;top:1985px;width:404px;height:336px;background:linear-gradient(135deg,#8d8f91,#c7b7a2 40%,#e6cf8e 55%,#6d6e70)}
.framed{padding:14px}
.framed-inner{border:1px solid #666;height:100%;padding:20px 20px}
.box-title{font:500 21px "Oswald",sans-serif;color:var(--white);letter-spacing:.5px;text-transform:uppercase}
.cert-list{list-style:none;margin-top:18px;font:400 12px "Open Sans",sans-serif;color:#ddd}
.cert-list li{margin-bottom:15px}
.btn{display:inline-block;background:var(--blue);color:var(--white);font:500 12px "Oswald",sans-serif;text-transform:uppercase;padding:7px 14px}

/* pricing */
.price-box{left:186px;top:2434px;width:404px;height:455px;background:var(--ink);padding:28px}
.price-inner{background:var(--white);height:100%;padding:20px 20px}
.price-table{width:100%;border-collapse:collapse;font:400 12px "Open Sans",sans-serif;color:#333}
.price-table td{border:1px solid #9dbfd0;padding:6px 7px;height:34px}
.price-table tr:nth-child(odd) td{background:var(--row)}
.price-table td:last-child{width:76px}
.consult{margin-top:10px;background:var(--ink);color:var(--white);text-align:center;font:500 22px/48px "Oswald",sans-serif;text-transform:uppercase}
.pic-frame{background:var(--ink);padding:8px}
.pic-fill{width:100%;height:100%}

/* aftercare */
.proc-list{list-style:none;margin-top:16px;font:400 12px/1.45 "Open Sans",sans-serif;color:#ddd}
.proc-list li{position:relative;padding-left:22px;margin-bottom:16px}
.proc-list li::before{content:"";position:absolute;left:2px;top:6px;width:7px;height:7px;border-radius:50%;background:var(--blue)}

/* newsletter */
.news{left:0;top:3510px;width:1200px;height:263px;background:linear-gradient(90deg,#151515,#3a3a3a 45%,#262626 70%,#111)}
.news-title{left:222px;top:3540px;font:500 24px "Oswald",sans-serif;color:var(--white);letter-spacing:1px}
.news-sub{left:222px;top:3590px;font:400 13px "Open Sans",sans-serif;color:#ddd}
.news-input{left:222px;top:3638px;width:672px;height:38px;background:#0b0b0b;border:none;font:400 13px "Open Sans",sans-serif;color:#aaa;padding:0 12px;line-height:38px}
.news-btn{left:898px;top:3638px;width:118px;height:38px;background:var(--blue);color:var(--white);font:500 13px/38px "Oswald",sans-serif;text-align:center;text-transform:uppercase}

/* contact */
.contact{left:0;top:3773px;width:1200px;height:415px;background:var(--sky)}
.contact-title{left:186px;top:3835px;width:206px;height:68px;border:2px solid var(--white);outline:1px solid var(--white);outline-offset:4px;
  font:500 22px/64px "Oswald",sans-serif;color:var(--white);text-align:center;text-transform:uppercase;letter-spacing:1px}
.field{height:30px;border:1px solid #555;background:var(--sky);font:400 12px/28px "Open Sans",sans-serif;color:#222;padding:0 8px}
.send{left:186px;top:4128px;width:88px;height:40px;background:var(--ink);color:var(--white);font:500 13px/40px "Oswald",sans-serif;text-align:center;letter-spacing:2px}
.info{left:683px;top:3920px;width:334px;height:248px;background:var(--ink);padding:8px}
.info-inner{border:1px solid #666;height:100%;padding:12px 16px}
.info-row{display:flex;gap:16px;margin-bottom:10px;align-items:flex-start}
.info-row svg{flex:none;margin-top:2px}
.info-label{font:500 13px "Oswald",sans-serif;color:var(--white);text-transform:uppercase}
.info-text{font:400 11px/1.4 "Open Sans",sans-serif;color:#ddd}

.footer{left:0;top:4188px;width:1200px;height:47px;background:var(--ink)}
.copyright{left:196px;top:4203px;font:400 12px "Open Sans",sans-serif;color:#ccc}
</style>
</head>
<body>

<!-- header & hero -->
<header class="abs hero"></header>
<div class="abs brand"><span class="brand-dot"></span><span class="brand-name">Velvet Ink Studio</span></div>
<nav class="abs nav">
  <span>HOME</span><span>SERVICES</span><span>ABOUT ROSALIND</span><span>PRICING</span><span>CONTACT US</span><span>PRE PROCEDURES</span><span>POST PROCEDURES</span>
</nav>
<div class="abs hero-art" role="img" aria-label="Portrait of a woman in soft makeup with pink orchids and butterflies"></div>
<div class="abs slogan slogan-1">Achieve your</div>
<div class="abs slogan slogan-2">Ideal Appearance</div>

<!-- special offer -->
<section class="abs offer"></section>
<svg class="abs offer-badge" viewBox="0 0 80 142"><path d="M0 0H80V122L40 142 0 122Z" fill="#2a9fd8"/><path d="M6 0V118L40 134 74 118V0" fill="none" stroke="#6cc3ee" stroke-width="2"/></svg>
<div class="abs offer-badge-text">SPECIAL<br>OFFER</div>
<div class="abs offer-text">Save Upto <b>50%</b> On Upper and Lower Eyeliner</div>

<!-- join / testimonials -->
<div class="abs tab" style="left:186px;top:825px">Join us</div>
<div class="abs tab" style="left:838px;top:825px">Testimonials</div>
<section class="abs panel" style="left:186px;top:884px;width:400px;height:260px"></section>
<div class="abs fb-box">
  <div class="fb-head">
    <span class="fb-thumb"></span>
    <span class="fb-title">Velvet Ink Studio</span>
    <span class="fb-likes">1,795 likes</span>
    <span class="fb-btn" style="left:8px">Like Page</span>
    <span class="fb-btn" style="right:8px">Book Now</span>
  </div>
  <div class="fb-photo" role="img" aria-label="Studio page cover photo of a client treatment"></div>
  <div class="fb-foot">Be the first of your friends to like this</div>
  <div class="fb-faces"><i></i><i></i><i></i><i></i><i></i><i></i><i></i><i></i></div>
</div>
<section class="abs panel" style="left:610px;top:884px;width:407px;height:260px"></section>
<p class="abs quote">Nemo enim ipsam voluptatem quia voluptas sit aspernatur aut odit aut fugit, sed quia consequuntur magni dolores eos qui ratione voluptatem sequi nesciunt neque porro quisquam est, qui dolorem ipsum quia dolor sit amet.</p>
<span class="abs arrow" style="left:622px;top:1000px">‹</span>
<span class="abs arrow" style="left:990px;top:1000px">›</span>
<div class="abs avatar" role="img" aria-label="Client portrait"></div>
<div class="abs quote-name">Tessa Lorne - ACD</div>

<!-- services -->
<div class="abs tab" style="left:186px;top:1203px">Our services</div>
<div class="abs services-sub">Semi - Permanent Makeup</div>
<section class="abs services-band"></section>

<article class="abs card" style="left:186px;top:1307px">
  <div class="card-top">
    <div class="card-head"><svg width="30" height="14" viewBox="0 0 30 14"><path d="M2 12Q14 0 28 6" stroke="#222" stroke-width="4" fill="none" stroke-linecap="round"/></svg><span class="card-title">Eyebrows</span></div>
    <p class="card-text">Duis aute irure dolor in reprehenderit in voluptate velit esse cillum dolore eu fugiat nulla pariatur.<b>[...]</b></p>
  </div>
  <div class="card-photo" role="img" aria-label="Before and after eyebrow photos"><span style="background:linear-gradient(#c89a80,#a77a62)"></span><span style="background:linear-gradient(#d0a58b,#b07d64)"></span></div>
  <div class="card-labels"><span>Before</span><span>After</span></div>
</article>
<article class="abs card" style="left:469px;top:1307px">
  <div class="card-top">
    <div class="card-head"><svg width="30" height="16" viewBox="0 0 30 16"><path d="M1 8Q15 -4 29 8Q15 20 1 8Z" fill="none" stroke="#222" stroke-width="2"/><circle cx="15" cy="8" r="4" fill="#222"/></svg><span class="card-title">Upper and Lower Eyeliner</span></div>
    <p class="card-text">Temporibus autem quibusdam et aut officiis debitis aut rerum necessitatibus saepe eveniet ut et voluptates.<b>[...]</b></p>
  </div>
  <div class="card-photo" role="img" aria-label="Before and after eyeliner photos"><span style="background:linear-gradient(#c9a08a,#9e7a68)"></span><span style="background:linear-gradient(#c49a86,#8f6d5c)"></span></div>
  <div class="card-labels"><span>Before</span><span>After</span></div>
</article>
<article class="abs card" style="left:751px;top:1307px">
  <div class="card-top">
    <div class="card-head"><svg width="30" height="14" viewBox="0 0 30 14"><path d="M1 7Q8 0 15 4Q22 0 29 7Q15 16 1 7Z" fill="#222"/></svg><span class="card-title">Lip Liner</span></div>
    <p class="card-text">Itaque earum rerum hic tenetur a sapiente delectus, ut aut reiciendis voluptatibus maiores alias consequatur.<b>[...]</b></p>
  </div>
  <div class="card-photo" role="img" aria-label="Before and after lip liner photos"><span style="background:linear-gradient(#d49a90,#b9706a)"></span><span style="background:linear-gradient(#d28580,#b35a5a)"></span></div>
  <div class="card-labels"><span>Before</span><span>After</span></div>
</article>

<article class="abs card" style="left:186px;top:1587px">
  <div class="card-top">
    <div class="card-head"><svg width="30" height="14" viewBox="0 0 30 14"><path d="M1 7Q8 0 15 4Q22 0 29 7Q15 16 1 7Z" fill="#222"/></svg><span class="card-title">Lip Blend</span></div>
    <p class="card-text">Duis aute irure vel eum iure reprehenderit qui ea voluptate velit esse quam nihil molestiae consequatur vel illum.<b>[...]</b></p>
  </div>
  <div class="card-photo" role="img" aria-label="Before and after lip blend photos"><span style="background:linear-gradient(#c7a08c,#9f7b68)"></span><span style="background:linear-gradient(#c99a84,#a4765e)"></span></div>
  <div class="card-labels"><span>Before</span><span>After</span></div>
</article>
<article class="abs card" style="left:469px;top:1587px">
  <div class="card-top">
    <div class="card-head"><svg width="26" height="20" viewBox="0 0 26 20"><path d="M3 18L16 5" stroke="#222" stroke-width="4" stroke-linecap="round"/><rect x="15" y="1" width="9" height="7" fill="#222" transform="rotate(-45 19 4)"/></svg><span class="card-title">Corrections</span></div>
    <p class="card-text">Duis aute irure dolor in reprehenderit in voluptate velit esse cillum dolore eu fugiat nulla pariatur.<b>[...]</b></p>
  </div>
  <div class="card-photo" role="img" aria-label="Before and after correction photos"><span style="background:linear-gradient(#bf9a86,#8d6f60)"></span><span style="background:linear-gradient(#c7a28d,#987763)"></span></div>
  <div class="card-labels"><span>Before</span><span>After</span></div>
</article>
<article class="abs card" style="left:751px;top:1587px">
  <div class="card-top">
    <div class="card-head"><svg width="22" height="22" viewBox="0 0 22 22"><rect x="2" y="2" width="18" height="18" fill="#222"/></svg><span class="card-title">Tattoo Removal</span></div>
    <p class="card-text">Excepteur sint occaecat cupidatat non proident, sunt in culpa qui officia deserunt mollit anim id est laborum.<b>[...]</b></p>
  </div>
  <div class="card-photo" role="img" aria-label="Before and after tattoo removal photos"><span style="background:linear-gradient(#b59480,#6f5a50)"></span><span style="background:linear-gradient(#d6b39c,#c49c84)"></span></div>
  <div class="card-labels"><span>Before</span><span>After</span></div>
</article>

<!-- about -->
<p class="abs about-intro">Rosalind completed her training with the Lumen Brow Academy Australia - Gold Coast, Queensland and Institute of Refined Skin &amp; Laser - Gold Coast, Queensland</p>
<div class="abs tab" style="left:807px;top:1929px">About Rosalind</div>
<div class="abs about-photo" role="img" aria-label="Portrait of Rosalind outdoors"></div>
<section class="abs panel framed" style="left:613px;top:1985px;width:404px;height:336px">
  <div class="framed-inner">
    <h2 class="box-title">Rosalind studied certificate</h2>
    <ul class="cert-list">
      <li>QRTMVNP617C – Design and perform cosmetic tattooing</li>
      <li>KMDPR719E – Maintain infection control standards in office practice setting</li>
      <li>JPWCFE118 – Provide First Aid</li>
      <li>Business Management - Frontline Management</li>
      <li>Graduate Diploma - Project Management</li>
    </ul>
    <div style="text-align:right;margin-top:-4px"><span class="btn">Read more</span></div>
  </div>
</section>

<!-- pricing -->
<div class="abs tab" style="left:186px;top:2378px">Pricing</div>
<div class="abs tab-note" style="left:328px;top:2398px">A follow-up appointment is included in all services within 4 to 6 weeks</div>
<section class="abs price-box">
  <div class="price-inner">
    <table class="price-table">
      <tr><td>Semi - Permanent Eyebrow Hairstrokes</td><td>$430.00</td></tr>
      <tr><td>Permanent Upper Eyeliner</td><td>$420.00</td></tr>
      <tr><td>Permanent Lower Eyeliner</td><td>$420.00</td></tr>
      <tr><td>Upper &amp; Lower Eyeliner together</td><td>$420.00</td></tr>
      <tr><td>Lip Liner</td><td>$360.00</td></tr>
      <tr><td>Lip Blend</td><td>$450.00</td></tr>
      <tr><td>Tattoo Removal session</td><td>$199.00</td></tr>
    </table>
    <div class="consult">Free consultation</div>
  </div>
</section>
<div class="abs pic-frame" style="left:610px;top:2434px;width:407px;height:455px">
  <div class="pic-fill" role="img" aria-label="Client relaxing during a treatment" style="background:linear-gradient(160deg,#d9dcd8,#a7a6a0 35%,#c9b3a2 60%,#e8e6e2)"></div>
</div>

<!-- aftercare -->
<div class="abs tab" style="left:186px;top:2945px">Aftercare procedures</div>
<div class="abs pic-frame" style="left:186px;top:3002px;width:404px;height:457px">
  <div class="pic-fill" role="img" aria-label="Artist performing an eyebrow procedure" style="background:linear-gradient(150deg,#f2efec,#d9b59a 40%,#7a5a48 70%,#3a2a22)"></div>
</div>
<section class="abs panel framed" style="left:610px;top:3002px;width:407px;height:457px">
  <div class="framed-inner" style="padding:22px 24px">
    <h2 class="box-title">Procedures</h2>
    <ul class="proc-list">
      <li>Duis aute irure dolor in reprehenderit in voluptate velit.</li>
      <li>Excepteur sint occaecat cupidatat non proident sunt in culpa qui officia deserunt.</li>
      <li>Temporibus autem quibusdam et aut officiis debitis aut rerum necessitatibus.</li>
      <li>Itaque earum rerum hic tenetur a sapiente delectus, ut aut reiciendis voluptatibus.</li>
      <li>Totam rem aperiam, eaque ipsa quae ab illo inventore veritatis et quasi.</li>
    </ul>
    <div style="text-align:right"><span class="btn">Read more</span></div>
  </div>
</section>

<!-- newsletter -->
<section class="abs news" role="img" aria-label="Dimmed photo of a treatment in progress"></section>
<h2 class="abs news-title">NEWSLETTER</h2>
<p class="abs news-sub">Subscribe to our newsletter for latest updates</p>
<div class="abs news-input">Email address...</div>
<div class="abs news-btn">Subscribe</div>

<!-- contact -->
<section class="abs contact"></section>
<h2 class="abs contact-title">Contact us</h2>
<div class="abs field" style="left:186px;top:3925px;width:260px">Name :</div>
<div class="abs field" style="left:458px;top:3925px;width:202px">Phone :</div>
<div class="abs field" style="left:186px;top:3979px;width:474px">Email :</div>
<div class="abs field" style="left:186px;top:4027px;width:474px;height:73px">Message :</div>
<div class="abs send">SEND</div>

<aside class="abs info">
  <div class="info-inner">
    <div class="info-row">
      <svg width="16" height="20" viewBox="0 0 16 20"><path d="M8 1C4 1 1 4 1 8c0 5 7 11 7 11s7-6 7-11c0-4-3-7-7-7z" fill="none" stroke="#fff" stroke-width="1.5"/><circle cx="8" cy="8" r="2.5" fill="#fff"/></svg>
      <div><div class="info-label">Location</div><div class="info-text">47 Fernleigh Crescent, Tui Harbour, 8093,<br>Christchurch</div></div>
    </div>
    <div class="info-row">
      <svg width="18" height="14" viewBox="0 0 18 14"><rect x="1" y="1" width="16" height="12" fill="none" stroke="#fff" stroke-width="1.5"/><path d="M1 1L9 8 17 1" fill="none" stroke="#fff" stroke-width="1.5"/></svg>
      <div><div class="info-label">Mail us</div><div class="info-text">velvetinkstudio@maildrop.example</div></div>
    </div>
    <div class="info-row">
      <svg width="18" height="18" viewBox="0 0 18 18"><path d="M4 1L7 5 5 7Q7 11 11 13L13 11 17 14 15 17Q7 17 1 4Z" fill="none" stroke="#fff" stroke-width="1.5"/></svg>
      <div><div class="info-label">Call us</div><div class="info-text">0219374620</div></div>
    </div>
    <div class="info-row">
      <svg width="16" height="16" viewBox="0 0 16 16"><circle cx="8" cy="8" r="7" fill="#fff"/></svg>
      <div class="info-label" style="font-size:11px">Velvet Ink Studio</div>
    </div>
  </div>
</aside>

<!-- footer -->
<footer class="abs footer"></footer>
<p class="abs copyright">© Copyright information here</p>

</body>
</html>
```